Creative Businesss Card desgin!

Create a business card for our business Gleam window cleaning!
We are open to creative ideas as long as it maintains a professional image.

Target Market(s)

Small Commercial window cleaning clients including car dealerships, strata manager, cafe

Industry/Entity Type

Window Cleaning

Contact Information for Business Card

Daniel Prescott
General Manager
Gleam Window Cleaning

daniel@gleamservices.com.au
pane-care-southbank.com.au
Ph: 1800 GET GLEAM
Mob: 0437 582 061

Colors
fbed22
0392cd

Requirements
Should not have
• Stock window cleaning/ squeegee graphics

```html
<!DOCTYPE html>
<html lang="en">
<head>
<meta charset="utf-8">
<title>Gleam Window Cleaning – Business Card</title>
<link href="https://fonts.googleapis.com/css2?family=Arimo:wght@400;700&display=swap" rel="stylesheet">
<style>
  :root{
    --yellow:#f5ec2a;
    --blue:#0b5687;
    --backdrop:#1d1d20;
    --card-w:560px;
    --card-h:320px;
  }
  *{box-sizing:border-box;margin:0;padding:0}
  html,body{width:1200px;height:800px;overflow:hidden;background:var(--backdrop)}
  body{position:relative;font-family:"Arimo",Arial,sans-serif}

  .card{position:absolute;width:var(--card-w);height:var(--card-h);overflow:hidden;box-shadow:0 14px 30px rgba(0,0,0,.45)}
  .card--front{left:70px;top:70px;background:var(--yellow)}
  .card--back{left:570px;top:410px;background:var(--blue)}

  .wordmark{font-weight:700;line-height:1;text-transform:uppercase}
  .wordmark__name{display:block;font-size:64px;letter-spacing:2px}
  .wordmark__sub{display:block;font-size:17px;letter-spacing:1px;margin-top:6px;text-align:right}
  .card--front .wordmark{position:absolute;left:50%;top:50%;transform:translate(-50%,-50%);color:var(--blue)}
  .card--back .wordmark{position:absolute;right:36px;top:34px;color:var(--yellow)}
  .card--back .wordmark__name{font-size:52px}
  .card--back .wordmark__sub{font-size:14px}

  .accent-dot{position:absolute;left:-24px;top:136px;width:48px;height:48px;border-radius:50%;background:var(--yellow)}
  .person{position:absolute;left:40px;top:138px;color:var(--yellow)}
  .person__name{font-weight:700;font-size:19px}
  .person__role{font-size:14px;margin-top:2px}

  .rule{position:absolute;left:40px;right:36px;top:220px;height:1px;background:var(--yellow)}
  .contacts{position:absolute;left:40px;right:36px;top:236px;display:flex;align-items:center;color:var(--yellow);font-size:13px}
  .contacts__group{display:flex;flex-direction:column;gap:7px}
  .contacts__divider{width:1px;height:36px;background:var(--yellow);margin:0 34px}
  .contact{display:flex;align-items:center;gap:7px}
  .contact svg{width:12px;height:12px;flex:none}
</style>
</head>
<body>

<section class="card card--front" aria-label="Card front">
  <div class="wordmark">
    <span class="wordmark__name">Gleam</span>
    <span class="wordmark__sub">Window Cleaning</span>
  </div>
</section>

<section class="card card--back" aria-label="Card back">
  <div class="wordmark">
    <span class="wordmark__name">Gleam</span>
    <span class="wordmark__sub">Window Cleaning</span>
  </div>

  <span class="accent-dot"></span>
  <div class="person">
    <p class="person__name">Daniel Prescott</p>
    <p class="person__role">General Manager</p>
  </div>

  <div class="rule"></div>

  <div class="contacts">
    <div class="contacts__group">
      <p class="contact">
        <svg viewBox="0 0 12 12" aria-hidden="true"><path fill="#f5ec2a" d="M2 1h2.5l1 2.5-1.4 1a6 6 0 0 0 3.4 3.4l1-1.4 2.5 1V10a1 1 0 0 1-1 1A9 9 0 0 1 1 2a1 1 0 0 1 1-1z"/></svg>
        1800 GET GLEAM
      </p>
      <p class="contact">
        <svg viewBox="0 0 12 12" aria-hidden="true"><rect x="3" y="0.7" width="6" height="10.6" rx="1" fill="none" stroke="#f5ec2a" stroke-width="1.2"/><circle cx="6" cy="9.4" r=".7" fill="#f5ec2a"/></svg>
        0437 582 061
      </p>
    </div>
    <span class="contacts__divider"></span>
    <div class="contacts__group">
      <p class="contact">
        <svg viewBox="0 0 12 12" aria-hidden="true"><rect x=".7" y="2.2" width="10.6" height="7.6" fill="none" stroke="#f5ec2a" stroke-width="1.2"/><path d="M.8 2.4 6 6.6l5.2-4.2" fill="none" stroke="#f5ec2a" stroke-width="1.2"/></svg>
        daniel@gleamservices.com.au
      </p>
      <p class="contact">
        <svg viewBox="0 0 12 12" aria-hidden="true"><g fill="none" stroke="#f5ec2a" stroke-width="1"><circle cx="6" cy="6" r="5.2"/><ellipse cx="6" cy="6" rx="2.2" ry="5.2"/><path d="M.8 6h10.4M1.8 3.3h8.4M1.8 8.7h8.4"/></g></svg>
        pane-care-southbank.com.au
      </p>
    </div>
  </div>
</section>

</body>
</html>
```